Velmora Water Purification

We need a website set up on a "Free account" WordPress platform. (This is the type of Wordpress site that you can sign up for and create online for free (not a server-hosted type.)
The website will be for a water purification company. They install devices in homes to purify the water for safer drinking, bathing, and cleaning.
Our logo is attached. Please keep color scheme of the website consistent with the logo.
Water Purification

```html
<!DOCTYPE html>
<html lang="en">
<head>
<meta charset="utf-8">
<title>Velmora Water Purification</title>
<link rel="stylesheet" href="https://fonts.googleapis.com/css2?family=Quicksand:wght@400;500;600&display=swap">
<style>
  :root {
    --night: #252538;
    --night-deep: #1b1b2a;
    --splash: #34344c;
    --band: #f3f3f5;
    --ink: #1f1f2b;
    --muted: #55556a;
    --accent-purple: #8a3fa3;
    --nav-active: #7c4a9e;
    --sky: #4aa9d9;
    --phone-blue: #3b6fb0;
    --title: #d9d9e0;
    --white: #ffffff;
    --brand-navy: #1c3f8f;
    --product-blue: #2f6fd0;
    --product-white: #e9edf3;
  }
  * { margin: 0; padding: 0; box-sizing: border-box; }
  html, body { width: 1200px; height: 662px; overflow: hidden; }
  body {
    font-family: "Quicksand", sans-serif;
    background: var(--night);
    position: relative;
  }
  .hero-splash {
    position: absolute; inset: 0;
    background:
      radial-gradient(ellipse 420px 180px at 640px 480px, var(--splash), transparent 70%),
      radial-gradient(ellipse 300px 160px at 980px 260px, var(--splash), transparent 70%),
      radial-gradient(ellipse 380px 140px at 180px 560px, #2e2e44, transparent 70%),
      linear-gradient(160deg, var(--night) 0%, var(--night) 40%, var(--night-deep) 100%);
  }
  .top-band {
    position: absolute; left: 0; top: 70px; width: 1200px; height: 55px;
    background: var(--band);
  }
  .main-nav {
    position: absolute; top: 70px; left: 0; height: 55px;
    display: flex; align-items: center;
  }
  .main-nav a {
    position: absolute; top: 21px;
    font-size: 11.5px; font-weight: 600; color: var(--ink);
    text-decoration: none; letter-spacing: 0.2px; white-space: nowrap;
  }
  .main-nav a.is-active { color: var(--nav-active); }
  .brand-badge {
    position: absolute; left: 541px; top: 32px; width: 126px; height: 104px;
    background: var(--white); border-radius: 50%;
    display: flex; align-items: center; justify-content: center;
  }
  .brand-name {
    font-size: 22px; font-weight: 600; color: var(--brand-navy);
  }
  .call-info {
    position: absolute; left: 738px; top: 92px;
    font-size: 11.5px; font-weight: 500; color: var(--muted); white-space: nowrap;
  }
  .call-icon { position: absolute; left: 940px; top: 88px; }
  .call-number {
    position: absolute; left: 966px; top: 91px;
    font-size: 11.5px; font-weight: 600; color: var(--phone-blue); letter-spacing: 0.3px;
  }
  .product {
    position: absolute; border-radius: 6px;
  }
  .product-left {
    left: 144px; top: 208px; width: 165px; height: 252px;
    background: linear-gradient(180deg, var(--product-blue) 0%, #1f5cc4 62%, var(--product-white) 63%, var(--white) 100%);
  }
  .product-right {
    left: 926px; top: 210px; width: 130px; height: 252px;
    background: linear-gradient(180deg, var(--white) 0%, var(--product-white) 55%, #9fb6dd 75%, #3c66c0 100%);
  }
  .hero-drop { position: absolute; left: 472px; top: 260px; }
  .hero-title {
    position: absolute; left: 0; width: 1200px; top: 280px;
    text-align: center; font-size: 56px; font-weight: 500; color: var(--title);
    line-height: 1;
  }
  .hero-tagline {
    position: absolute; left: 0; width: 1200px; top: 364px;
    text-align: center; font-size: 30px; font-weight: 400; color: var(--white);
    line-height: 1;
  }
  .hero-tagline span { color: var(--sky); }
  .feature {
    position: absolute; top: 516px; width: 180px; margin-left: -90px;
    text-align: center;
  }
  .feature-icon {
    width: 50px; height: 50px; border-radius: 50%;
    background: var(--accent-purple); margin: 0 auto;
    display: flex; align-items: center; justify-content: center;
  }
  .feature-label {
    margin-top: 17px; font-size: 14px; font-weight: 500; color: var(--white);
  }
</style>
</head>
<body>
  <div class="hero-splash" role="img" aria-label="Dark water splash with bubbles flowing across the background"></div>

  <div class="top-band"></div>
  <nav class="main-nav">
    <a href="#" class="is-active" style="left:143px">HOME</a>
    <a href="#" style="left:200px">ABOUT</a>
    <a href="#" style="left:263px">HISTORY</a>
    <a href="#" style="left:336px">PRODUCTS</a>
    <a href="#" style="left:421px">CONTACTS</a>
  </nav>

  <div class="brand-badge"><span class="brand-name">Velmora</span></div>

  <div class="call-info">YOUR FIRST VISIT? CALL FOR INFO</div>
  <svg class="call-icon" width="20" height="20" viewBox="0 0 20 20" aria-hidden="true">
    <path d="M4 2 l3 0 l1.5 4 l-2 1.5 a10 10 0 0 0 6 6 l1.5 -2 l4 1.5 l0 3 a2 2 0 0 1 -2 2 A15 15 0 0 1 2 4 a2 2 0 0 1 2 -2z" fill="var(--ink)"/>
  </svg>
  <div class="call-number">+1-555-014-2290</div>

  <div class="product product-left" role="img" aria-label="Blue and white wall-mounted water purifier"></div>
  <div class="product product-right" role="img" aria-label="White countertop water purifier with blue base"></div>

  <svg class="hero-drop" width="20" height="28" viewBox="0 0 20 28" aria-hidden="true">
    <path d="M10 0 C10 6 19 13 19 19 a9 9 0 0 1 -18 0 C1 13 10 6 10 0z" fill="var(--sky)"/>
  </svg>
  <h1 class="hero-title">Velmora</h1>
  <p class="hero-tagline">The Best Water <span>Right At Your Home</span></p>

  <div class="feature" style="left:248px">
    <div class="feature-icon">
      <svg width="20" height="30" viewBox="0 0 20 30" aria-hidden="true">
        <rect x="4" y="0" width="12" height="6" rx="2" fill="#fff"/>
        <rect x="2" y="8" width="16" height="22" rx="1" fill="#fff"/>
        <rect x="6" y="16" width="8" height="6" fill="var(--accent-purple)"/>
      </svg>
    </div>
    <div class="feature-label">Aesthetics Friendly</div>
  </div>
  <div class="feature" style="left:478px">
    <div class="feature-icon">
      <svg width="18" height="32" viewBox="0 0 18 32" aria-hidden="true">
        <rect x="6" y="0" width="6" height="4" fill="#fff"/>
        <path d="M5 5 h8 l3 6 v21 h-14 v-21z" fill="#fff"/>
        <path d="M9 15 c0 2 3 4 3 6 a3 3 0 0 1 -6 0 c0 -2 3 -4 3 -6z" fill="var(--accent-purple)"/>
      </svg>
    </div>
    <div class="feature-label">Best Quallity</div>
  </div>
  <div class="feature" style="left:712px">
    <div class="feature-icon">
      <svg width="22" height="32" viewBox="0 0 22 32" aria-hidden="true">
        <path d="M3 0 h16 v12 l-8 4 l-8 -4z" fill="#fff"/>
        <rect x="2" y="16" width="18" height="16" rx="2" fill="#fff"/>
        <rect x="7" y="20" width="8" height="6" fill="var(--accent-purple)"/>
      </svg>
    </div>
    <div class="feature-label">Easy to Install</div>
  </div>
  <div class="feature" style="left:945px">
    <div class="feature-icon">
      <svg width="22" height="28" viewBox="0 0 22 28" aria-hidden="true">
        <path d="M1 0 h20 l-2 28 h-16z" fill="#fff"/>
        <path d="M5 8 h12 l-1.5 16 h-9z" fill="var(--accent-purple)"/>
      </svg>
    </div>
    <div class="feature-label">100% Pure water</div>
  </div>
</body>
</html>
```